Book Cover Design Project

NOTE. I need the design in four days of posting this!

This will be the cover of my first book, WALK THE HIGH LINE -
MEANING AT THE CORE OF EVERY VENTURE. The book explains defines what Purpose and Meaning is, and how to use it in business. I have included the first chapter to provide a background.

I want the core colours to be black and white, and use the colours Violet, Cerulean Blue Extra Pale (powder blue), Cadmium Lemon (flouro yellow). I plan on using this design as the basis for future books in the WALK THE HIGH LINE series, where the yellow is carried through but the violet and blue colours changing.

This is a spiritual business book without using any spiritual language. It is strongly masculine and direct in its nature.

What I am looking for is something Remarkable that captures my reader immediately. My reader is a seeker. He/she is an entrepreneur perhaps looking to setup a new venture and looking for new and better ways of doing things, or he/she may be a small/medium business owner perhaps bored looking for more meaning in personal and business life), or the corporate person who is looking to get out and do something new. Age 35-50.
Updates

Hi I want to correct the paper size. It is "C Format" (trade paperbacks) are 135mm x 216mm (5.32" x 8.51").

Thks

Reason: A deadline has changed which means the completion of this book cover is less time-critical.

This is a business book that introduces new concepts, such as Purpose. Although it is based on spiritual principals  it is using normal business language when explaining what Purpose is, and how businesses can identify it and use it to be more successful.

If there is a border between a self-help and a business book, this book sits close to the border but markedly on the business side.

Hi I want to confirm the book size. The book size I require is the Australian C Format, which measures 153mm W x 234mm H. 

Sorry for any confusion

Reason: Hi I have extended the deadline as I want to be able to print prospective covers and see how they look like in a bookshop next to other covers.

Reason: To allow for final negotiations.

Industry/Entity Type

Business

```html
<!DOCTYPE html>
<html lang="en">
<head>
<meta charset="utf-8">
<title>Walk the High Line — Book Cover</title>
<link rel="stylesheet" href="https://fonts.googleapis.com/css2?family=Montserrat:wght@400;700;800&family=Raleway:wght@200;300&family=Crimson+Text:ital@1&display=swap">
<style>
  :root {
    --backdrop: #c4c4c4;
    --paper: #ffffff;
    --ink: #231f20;
    --lemon: #f5f064;
    --powder-blue: #96d6f2;
    --violet: #b86fae;
  }
  * { margin: 0; padding: 0; box-sizing: border-box; }
  html, body {
    width: 1200px;
    height: 900px;
    overflow: hidden;
    background: var(--backdrop);
  }
  .cover {
    position: absolute;
    left: 366px;
    top: 33px;
    width: 517px;
    height: 823px;
    background: var(--paper);
  }
  .series-block {
    position: absolute;
    left: 0;
    top: 24px;
    width: 199px;
    height: 206px;
    background: var(--lemon);
    color: var(--ink);
    font-family: "Montserrat", sans-serif;
    padding: 68px 0 0 20px;
  }
  .series-block .series-lead {
    display: block;
    font-weight: 400;
    font-size: 24px;
    line-height: 1;
    letter-spacing: 0.2px;
  }
  .series-block .series-name {
    display: block;
    font-weight: 800;
    font-size: 27px;
    line-height: 1.1;
    letter-spacing: 0.3px;
    margin-top: 4px;
  }
  .subtitle-block {
    position: absolute;
    left: 0;
    top: 255px;
    width: 199px;
    height: 243px;
    background: var(--ink);
  }
  .subtitle-block svg { display: block; }
  .subtitle-text {
    fill: var(--paper);
    font-family: "Raleway", sans-serif;
    font-weight: 200;
  }
  .line-one { font-size: 34px; }
  .line-two { font-size: 27px; }
  .line-three { font-size: 38px; }
  .line-four { font-size: 45px; }
  .author {
    position: absolute;
    left: 101px;
    top: 626px;
    font-family: "Crimson Text", serif;
    font-style: italic;
    font-size: 17.5px;
    color: var(--ink);
  }
  .artwork {
    position: absolute;
    left: 0;
    top: 0;
  }
  .figure-area { fill: var(--ink); }
  .triangle-blue { fill: none; stroke: var(--powder-blue); stroke-width: 13; stroke-linejoin: miter; }
  .triangle-violet { fill: none; stroke: var(--violet); stroke-width: 10; stroke-linejoin: miter; }
  .triangle-violet-fine { fill: none; stroke: var(--violet); stroke-width: 1.5; }
</style>
</head>
<body>
  <main class="cover">
    <div class="series-block">
      <span class="series-lead">WALK THE</span>
      <span class="series-name">HIGH LINE</span>
    </div>

    <h1 class="subtitle-block" aria-label="Meaning at the core of every venture">
      <svg width="199" height="243" viewBox="0 0 199 243" aria-hidden="true">
        <text class="subtitle-text line-one" x="15" y="74" textLength="158" lengthAdjust="spacingAndGlyphs">MEANING</text>
        <text class="subtitle-text line-two" x="15" y="109" textLength="158" lengthAdjust="spacingAndGlyphs">AT THE CORE</text>
        <text class="subtitle-text line-three" x="15" y="152" textLength="163" lengthAdjust="spacingAndGlyphs">OF EVERY</text>
        <text class="subtitle-text line-four" x="15" y="194" textLength="166" lengthAdjust="spacingAndGlyphs">VENTURE</text>
      </svg>
    </h1>

    <svg class="artwork" width="517" height="823" viewBox="0 0 517 823">
      <polygon class="triangle-blue" points="223,264 460,367 223,490"/>
      <polygon class="triangle-violet-fine" points="439,552 439,719 250,645"/>
      <rect class="figure-area" x="242" y="262" width="174" height="465" rx="6"
            role="img" aria-label="Silhouette of a headless man in a dark business suit and tie, hands in pockets"/>
      <polygon class="triangle-violet" points="230,632 428,532 428,722"/>
    </svg>

    <p class="author">Anders Holmqvist</p>
  </main>
</body>
</html>
```